RidgeHornSupply.com

I need a new webdesign for a company in the Ridge Horn/SF Bay area that showcases the financial benefits of buying used band instruments for junior high students.This would be opposed to the current and costly option of renting cheap quality instruments from the 2 or 3 local music stores that charge a monthly fee that over the years charges the buyer 3 or 4x over..
Instruments: focus in on Alto Sax, Trumpet, Flute, Clarinet, Trombone, Tenor Sax, Baritone
Target middle schools are Kestrelwood Middle School and Harlow Middle School in Ridge Horn, CA. Both have award winning band programs.
Files attached may or may not be important.
Tabs Needed and funtional
Contact
Shopping Cart
Select Instrument
Checkout
Add to Cart, etc.
Instuments
quantity, etc.
trade in your instrument/sell your instrument
ability to add or take away new instruments for sale. including pictures
Additional questions or info, feel free to ask
Hi Designers,
Project Deadline Extended
Reason: In the next week you will be receiving specific content that will be required to be had on the website.
New desigins are still welcome. Please continue to contact me if you have questions about your individual designs.
Thanks!
Ridge Horn

```html
<!DOCTYPE html>
<html lang="en">
<head>
<meta charset="utf-8">
<title>Ridge Horn – Band Instruments</title>
<link rel="stylesheet" href="https://fonts.googleapis.com/css2?family=Jost:wght@300;400;500&family=Montserrat:wght@400;500&display=swap">
<style>
:root{
  --green:#7cb51c;
  --green-dark:#5f9410;
  --ink:#3a3a3a;
  --muted:#8a8a8a;
  --topbar:#2a2a2a;
  --footer:#1f1f1f;
  --bottom:#f3f3f1;
  --page:#f1f1ef;
  --white:#fff;
}
*{box-sizing:border-box;margin:0;padding:0}
html,body{width:958px;height:1200px;overflow:hidden}
body{position:relative;background:var(--page);font-family:"Jost",sans-serif;color:var(--ink)}
.abs{position:absolute}

/* top bar */
.topbar{left:0;top:0;width:958px;height:27px;background:var(--topbar)}
.account-links{left:128px;top:0;height:27px;display:flex;gap:20px;align-items:center;font-size:9px;color:#9a9a9a}
.account-links span::before{content:"";display:inline-block;width:6px;height:6px;background:#777;margin-right:5px;border-radius:1px}
.search{left:626px;top:4px;width:112px;height:19px;border-radius:10px;background:#1a1a1a;font-size:9px;color:#8a8a8a;padding:4px 11px}
.search svg{position:absolute;right:9px;top:5px}
.cart-pill{left:744px;top:4px;width:85px;height:19px;border-radius:10px;background:#1a1a1a;font-size:9px;color:#fff;font-weight:500;padding:4px 0 0 28px}
.cart-pill b{color:var(--green);margin-left:6px}
.cart-pill svg{position:absolute;left:11px;top:5px}

/* nav */
.navbar{left:0;top:27px;width:958px;height:45px;background:var(--white);border-bottom:1px solid #ddd}
.brand{left:128px;top:37px;font-size:20px;font-weight:300;color:var(--ink);letter-spacing:.5px}
.menu{left:328px;top:27px;height:45px;display:flex;font-family:"Montserrat",sans-serif;font-size:9.5px;color:#666;letter-spacing:.3px}
.menu a{display:flex;align-items:center;padding:0 13px;border-right:1px solid #e4e4e4;text-decoration:none;color:inherit}

/* hero */
.hero{left:0;top:72px;width:958px;height:393px;background:linear-gradient(90deg,#1d1614 0%,#3a2c27 35%,#2b211d 60%,#4a3a34 85%,#231b18 100%)}
.hero-title{left:129px;top:194px;font-size:30px;font-weight:400;color:#fff;letter-spacing:1px}
.hero-rule{left:130px;top:243px;width:397px;height:1px;background:#ddd}
.hero-text{left:130px;top:258px;width:410px;font-family:"Montserrat",sans-serif;font-size:11.2px;line-height:16.5px;color:#fff;font-weight:500}
.shop-btn{left:130px;top:324px;width:156px;height:31px;border-radius:16px;background:linear-gradient(#8cc628,var(--green-dark));color:#fff;font-size:17px;padding:4px 0 0 22px}
.shop-btn svg{position:absolute;right:12px;top:8px}

/* partner strip */
.partners{left:0;top:465px;width:958px;height:40px;background:var(--white);border-bottom:1px solid #ddd}
.partner-row{left:128px;top:465px;height:40px;display:flex}
.partner-row span{width:88px;height:40px;display:flex;align-items:center;justify-content:center;border-left:1px solid #e2e2e2;font-size:12px;font-weight:500;color:#666}
.partner-row span:last-child{border-right:1px solid #e2e2e2}

/* instruments */
.section-title{left:0;top:531px;width:958px;text-align:center;font-size:29px;font-weight:300;color:var(--ink)}
.section-title em{font-style:normal;color:var(--green)}
.section-rule{left:128px;top:573px;width:701px;height:2px;border-top:1px solid #bdbdbd;border-bottom:1px solid #e0e0e0}
.section-text{left:128px;top:587px;width:701px;text-align:center;font-family:"Montserrat",sans-serif;font-size:10px;line-height:14.5px;color:var(--muted)}
.tile{width:172px;height:123px;overflow:hidden}
.tile.tall{height:249px}
.tile .photo{position:absolute;inset:0}
.tile .label{position:absolute;left:0;bottom:0;width:100%;height:27px;background:rgba(25,25,25,.88);color:#fff;font-size:15px;padding:3px 0 0 13px;letter-spacing:.5px}
.tile .add{position:absolute;right:0;bottom:0;width:27px;height:27px;background:var(--green);display:flex;align-items:center;justify-content:center}

/* footer */
.footer{left:0;top:939px;width:958px;height:219px;background:repeating-linear-gradient(45deg,var(--footer) 0 3px,#232323 3px 6px)}
.foot-title{position:absolute;font-size:17px;font-weight:400;color:#fff;white-space:nowrap}
.sitemap{left:128px;top:1004px;font-family:"Montserrat",sans-serif;font-size:9.5px;line-height:18.4px;color:#999;list-style:none}
.sitemap li:first-child{color:#fff}
.about-text{left:282px;top:1006px;width:292px;font-family:"Montserrat",sans-serif;font-size:9px;line-height:13px;color:#999}
.read-more{left:283px;top:1107px;width:74px;height:23px;background:var(--green);color:#fff;font-size:11px;text-align:center;padding-top:4px}
.cards{left:624px;top:1006px;display:flex;gap:5px}
.cards i{display:block;width:28px;height:16px;border-radius:2px}
.news-text{left:624px;top:1071px;width:200px;font-family:"Montserrat",sans-serif;font-size:9px;line-height:13px;color:#9a9a9a;font-weight:500}
.email{left:625px;top:1106px;width:131px;height:24px;background:#fff;border:1px solid #ccc;font-size:8px;font-style:italic;color:#999;padding:5px 0 0 13px}
.subscribe{left:756px;top:1106px;width:74px;height:24px;background:var(--green);color:#fff;font-size:11px;text-align:center;padding-top:5px}

/* bottom */
.bottom{left:0;top:1158px;width:958px;height:42px;background:var(--bottom)}
.copyright{left:128px;top:1171px;font-family:"Montserrat",sans-serif;font-size:9.5px;color:#666}
.social{left:710px;top:1166px;display:flex;gap:5px}
.social i{display:block;width:20px;height:20px;border-radius:50%;border:1.5px solid #777}
</style>
</head>
<body>

<div class="abs topbar"></div>
<div class="abs account-links"><span>My Wishlist</span><span>My Account</span><span>Log in</span></div>
<div class="abs search">Search
  <svg width="9" height="9" viewBox="0 0 10 10"><circle cx="4" cy="4" r="3" fill="none" stroke="#7cb51c" stroke-width="1.5"/><line x1="6.3" y1="6.3" x2="9" y2="9" stroke="#7cb51c" stroke-width="1.6"/></svg>
</div>
<div class="abs cart-pill">
  <svg width="13" height="9" viewBox="0 0 13 9"><path d="M0 1h2.5l2 5h6l1.5-4H3.5" fill="none" stroke="#ccc" stroke-width="1.2"/><circle cx="5" cy="8" r="1" fill="#ccc"/><circle cx="10" cy="8" r="1" fill="#ccc"/></svg>
  CART<b>0</b> ▾
</div>

<div class="abs navbar"></div>
<div class="abs brand">RIDGE HORN</div>
<nav class="abs menu">
  <a href="#">HOME</a><a href="#">INSTRUMENT</a><a href="#">CHECKOUT</a><a href="#">QUANTITY</a><a href="#">SHOPPING CART</a><a href="#">CONTACT US</a>
</nav>

<div class="abs hero" role="img" aria-label="Photo of student musicians playing clarinets on a stage"></div>
<div class="abs hero-title">WELCOME TO RIDGE HORN</div>
<div class="abs hero-rule"></div>
<p class="abs hero-text">LOREM IPSUM IS SIMPLY DUMMY TEXT OF TYPESETTING INDUSTRY. LOREM IPSUM HAS BEEN THE INDUSTRY'S STANDARD DUMMY TEXT EVER SINCE THE 1500S.</p>
<div class="abs shop-btn">SHOP NOW
  <svg width="15" height="15" viewBox="0 0 15 15"><circle cx="7.5" cy="7.5" r="7.5" fill="#fff"/><path d="M6 4.5l3 3-3 3" fill="none" stroke="#6aa516" stroke-width="2"/></svg>
</div>

<div class="abs partners"></div>
<div class="abs partner-row">
  <span>Norvale</span><span>Lumera</span><span>Corelay</span><span>Stonegate</span><span>Tavern</span><span>Brightly</span><span>Cardwell</span><span>Crumbo</span>
</div>

<h2 class="abs section-title">OUR <em>INSTRUMENT</em></h2>
<div class="abs section-rule"></div>
<p class="abs section-text">Lorem Ipsum is simply dummy text of typesetting industry. Lorem Ipsum has been. the industry's standard dummy text ever since the 1500s, when an unknown printer took a galley of type and scrambled it to make a type specimen book.</p>

<div class="abs tile" style="left:130px;top:642px"><div class="photo" role="img" aria-label="Alto saxophone" style="background:linear-gradient(135deg,#d9d7dc,#b9a98a)"></div><div class="label">ALTO SAX</div><div class="add"><svg width="15" height="12" viewBox="0 0 15 12"><path d="M0 1h3l2 6h7l2-5H4" fill="none" stroke="#fff" stroke-width="1.5"/><circle cx="6" cy="10.5" r="1.2" fill="#fff"/><circle cx="11" cy="10.5" r="1.2" fill="#fff"/></svg></div></div>
<div class="abs tile" style="left:305px;top:642px"><div class="photo" role="img" aria-label="Trumpet" style="background:linear-gradient(180deg,#d8d8d8,#a9a49c)"></div><div class="label">TRUMPET</div><div class="add"><svg width="15" height="12" viewBox="0 0 15 12"><path d="M0 1h3l2 6h7l2-5H4" fill="none" stroke="#fff" stroke-width="1.5"/><circle cx="6" cy="10.5" r="1.2" fill="#fff"/><circle cx="11" cy="10.5" r="1.2" fill="#fff"/></svg></div></div>
<div class="abs tile" style="left:480px;top:642px"><div class="photo" role="img" aria-label="Flutes laid side by side" style="background:linear-gradient(135deg,#e4e2dc,#c2b79f)"></div><div class="label">FLUTE</div><div class="add"><svg width="15" height="12" viewBox="0 0 15 12"><path d="M0 1h3l2 6h7l2-5H4" fill="none" stroke="#fff" stroke-width="1.5"/><circle cx="6" cy="10.5" r="1.2" fill="#fff"/><circle cx="11" cy="10.5" r="1.2" fill="#fff"/></svg></div></div>
<div class="abs tile tall" style="left:655px;top:642px"><div class="photo" role="img" aria-label="Clarinets standing upright" style="background:linear-gradient(90deg,#d8d4cf,#bfb8ae 50%,#d6d1c9)"></div><div class="label">CLARINET</div><div class="add"><svg width="15" height="12" viewBox="0 0 15 12"><path d="M0 1h3l2 6h7l2-5H4" fill="none" stroke="#fff" stroke-width="1.5"/><circle cx="6" cy="10.5" r="1.2" fill="#fff"/><circle cx="11" cy="10.5" r="1.2" fill="#fff"/></svg></div></div>
<div class="abs tile" style="left:130px;top:768px"><div class="photo" role="img" aria-label="Trombone" style="background:linear-gradient(135deg,#d6cfc2,#b09d78)"></div><div class="label">TROMBONE</div><div class="add"><svg width="15" height="12" viewBox="0 0 15 12"><path d="M0 1h3l2 6h7l2-5H4" fill="none" stroke="#fff" stroke-width="1.5"/><circle cx="6" cy="10.5" r="1.2" fill="#fff"/><circle cx="11" cy="10.5" r="1.2" fill="#fff"/></svg></div></div>
<div class="abs tile" style="left:305px;top:768px"><div class="photo" role="img" aria-label="Tenor saxophone" style="background:linear-gradient(135deg,#d5d3d3,#b39a5c)"></div><div class="label">TENOR SAX</div><div class="add"><svg width="15" height="12" viewBox="0 0 15 12"><path d="M0 1h3l2 6h7l2-5H4" fill="none" stroke="#fff" stroke-width="1.5"/><circle cx="6" cy="10.5" r="1.2" fill="#fff"/><circle cx="11" cy="10.5" r="1.2" fill="#fff"/></svg></div></div>
<div class="abs tile" style="left:480px;top:768px"><div class="photo" role="img" aria-label="Baritone horn" style="background:linear-gradient(180deg,#cfcfcf,#a8a08e)"></div><div class="label">BARITONE</div><div class="add"><svg width="15" height="12" viewBox="0 0 15 12"><path d="M0 1h3l2 6h7l2-5H4" fill="none" stroke="#fff" stroke-width="1.5"/><circle cx="6" cy="10.5" r="1.2" fill="#fff"/><circle cx="11" cy="10.5" r="1.2" fill="#fff"/></svg></div></div>

<div class="abs footer"></div>
<h3 class="foot-title" style="left:128px;top:974px">Site Map</h3>
<ul class="abs sitemap"><li>Home</li><li>About us</li><li>Instrument</li><li>Checkout</li><li>Quantity</li><li>Shopping cart</li><li>Contact Us</li></ul>
<h3 class="foot-title" style="left:282px;top:974px">About Us</h3>
<p class="abs about-text">Lorem Ipsum is simply dummy text of the printing and typesetting industry. Lorem Ipsum has been the industry's standard dummy text ever since the 1500s, when an unknown printer took a galley of type and scrambled it to make a type specimen book. It has survived not only five centuries, but also the leap into electronic typesetting, remaining essentially unchanged. It was popularised in the 1960s with the release.</p>
<div class="abs read-more">Read More</div>
<h3 class="foot-title" style="left:623px;top:974px">Payment Option</h3>
<div class="abs cards"><i style="background:#f2f2f2"></i><i style="background:#2b2b2b;border:1px solid #555"></i><i style="background:#e8e8e8"></i><i style="background:#d9d9d9"></i><i style="background:#4a78b8"></i></div>
<h3 class="foot-title" style="left:623px;top:1042px">Signup to Our Newsletters</h3>
<p class="abs news-text">Lorem Ipsum is simply dummy text of the printing and typesetting industry.</p>
<div class="abs email">E-mail Address</div>
<div class="abs subscribe">Subscribe</div>

<div class="abs bottom"></div>
<div class="abs copyright">© 2014 Ridge Horn. All Rights Reserved. Terms &amp; conditions</div>
<div class="abs social"><i></i><i></i><i></i><i></i><i></i></div>

</body>
</html>
```